Dean Hollis Business Card

In addition to my name design (file uploaded), black print on white card stock, e-mail address should be presented as a typical e-mail address, i.e., underlined and in blue ink, the card should include the following information:
Professor of Aviation Technology
Accident Litigation Expert Witness
Master Certificated Flight Instructor

dhollis@vexmail.example
Anchorage, Alaska
(907) 318-5074

```html
<!DOCTYPE html>
<html lang="en">
<head>
<meta charset="utf-8">
<title>Dean Hollis Business Card</title>
<link rel="stylesheet" href="https://fonts.googleapis.com/css2?family=Arimo:wght@400&display=swap">
<style>
  :root {
    --card: #ffffff;
    --ink: #000000;
    --rule: #3f86c8;
    --link: #1565c8;
    --plane-dark: #7b7b7b;
    --plane-mid: #a9a9a9;
    --plane-light: #c9c9c9;
  }
  * { margin: 0; padding: 0; box-sizing: border-box; }
  html, body {
    width: 1200px;
    height: 737px;
    overflow: hidden;
    background: var(--card);
  }
  .card {
    position: relative;
    width: 1200px;
    height: 737px;
    background: var(--card);
    font-family: "Arimo", Arial, sans-serif;
    color: var(--ink);
    overflow: hidden;
  }
  .name-mark {
    position: absolute;
    left: 213px;
    width: 691px;
    top: 30px;
    height: 100px;
    display: flex;
    align-items: center;
    justify-content: center;
    font-size: 84px;
    font-weight: 400;
    letter-spacing: 2px;
    line-height: 1;
    color: var(--ink);
    white-space: nowrap;
    z-index: 2;
  }
  .header-rule {
    position: absolute;
    left: 0;
    top: 150px;
    width: 1200px;
    height: 5px;
    background: var(--rule);
  }
  .plane {
    position: absolute;
    border-radius: 50%;
    z-index: 1;
  }
  .plane--dark { background: radial-gradient(ellipse at center, var(--plane-dark) 0%, var(--plane-dark) 35%, rgba(123,123,123,0) 70%); }
  .plane--mid { background: radial-gradient(ellipse at center, var(--plane-mid) 0%, var(--plane-mid) 35%, rgba(169,169,169,0) 70%); }
  .plane--light { background: radial-gradient(ellipse at center, var(--plane-light) 0%, var(--plane-light) 35%, rgba(201,201,201,0) 70%); }

  .credentials {
    position: absolute;
    left: 44px;
    top: 259px;
    z-index: 2;
  }
  .credentials__title {
    font-size: 33px;
    font-weight: 400;
    line-height: 40px;
  }
  .credentials__role {
    font-size: 24px;
    line-height: 38px;
    padding-left: 3px;
  }
  .contact {
    position: absolute;
    left: 49px;
    top: 436px;
    z-index: 2;
    font-size: 33px;
    line-height: 43px;
    font-style: normal;
  }
  .contact__email {
    color: var(--link);
    text-decoration: underline;
    text-underline-offset: 4px;
    text-decoration-thickness: 2px;
  }
</style>
</head>
<body>
  <main class="card">
    <div class="name-mark">DEAN E HOLLIS</div>
    <div class="header-rule"></div>

    <div class="plane plane--mid" role="img" aria-label="Airplane silhouette" style="left:1025px;top:46px;width:103px;height:83px;"></div>
    <div class="plane plane--light" role="img" aria-label="Small airplane silhouette" style="left:517px;top:128px;width:28px;height:40px;"></div>
    <div class="plane plane--light" role="img" aria-label="Small airplane silhouette" style="left:674px;top:150px;width:26px;height:40px;"></div>
    <div class="plane plane--mid" role="img" aria-label="Airplane silhouette" style="left:794px;top:208px;width:100px;height:84px;"></div>
    <div class="plane plane--light" role="img" aria-label="Small airplane silhouette" style="left:293px;top:311px;width:33px;height:33px;"></div>
    <div class="plane plane--dark" role="img" aria-label="Large airplane silhouette" style="left:454px;top:305px;width:208px;height:164px;"></div>
    <div class="plane plane--light" role="img" aria-label="Airplane silhouette" style="left:218px;top:457px;width:70px;height:66px;"></div>
    <div class="plane plane--mid" role="img" aria-label="Small airplane silhouette" style="left:642px;top:564px;width:46px;height:40px;"></div>
    <div class="plane plane--mid" role="img" aria-label="Small airplane silhouette" style="left:1048px;top:564px;width:62px;height:54px;"></div>
    <div class="plane plane--mid" role="img" aria-label="Airplane silhouette" style="left:65px;top:618px;width:100px;height:82px;"></div>

    <section class="credentials">
      <h1 class="credentials__title">Professor of Aviation Technology</h1>
      <p class="credentials__role">Accident Litigation Expert Witness</p>
      <p class="credentials__role">Master Certificated Flight Instructor</p>
    </section>

    <address class="contact">
      <div class="contact__email">dhollis@vexmail.example</div>
      <div class="contact__city">Anchorage, Alaska</div>
      <div class="contact__phone">(907) 318-5074</div>
    </address>
  </main>
</body>
</html>
```